Door Hanger Design for Electricians Serving Homes

I would like our logo incorporated into the door hanger. We would like a place for a tear off section on the bottom of the hanger with our contact information: K&T Electric - (555) 318-4702 - www.kandtelectric.example - info@kandtelectric.example.
Door Hanger Script
Front Side of the Door Hanger:
[Company Logo]
Need a Reliable Electrician?
Your Local Electrical Expert is Just Around the Corner!
• Quick Response Times
• Affordable Rates
• Quality Workmanship
• Fully Licensed & Insured
• Special Offer:
• 10% OFF Your First Service Call!
Back Side of the Door Hanger:
Don't Let Electrical Issues Keep You in the Dark!
From flickering lights to complete system upgrades, we've got all your
residential electrical needs covered. Our services include:
• Electrical Repairs & Troubleshooting
• Lighting Installation & Upgrades
• Safety Inspections & Code Compliance
• Energy-Efficient Solutions
• 24/7 Emergency Services
• Why Choose Us?
• Friendly, Local Service
• Over 30 Years of Experience
• Satisfaction Guaranteed
• Upfront Pricing
Call Us Today: [Your Phone Number]
Visit Our Website: [Your Website]
Book Your Appointment Now and Claim Your 10% Discount!
Offer valid for new customers on the first visit only. Mention this door hanger when
booking.
[Your Company Name and Contact Information]
Follow Us on Social Media for More Tips and Special Offers!
[Icons for social media platforms: Chatterpage, Pixmosaic, Quibbler, etc.]
Design Tips:
Use bold, clear fonts for easy reading.
Incorporate your brand colors and logo for instant recognition.
Include a clear call to action (CTA) on both sides.
Add a tear-off section at the bottom with your contact information for
convenience.
Use high-quality images or graphics related to electrical work to catch
the eye.
This door hanger design and copy aim to attract residential clients by
highlighting the benefits of your electrical services, special offers, and
how they can easily get in touch with you for their electrical needs.
The door knocker template will have three of the same design on front and three of the same design on the back. This template is from the print shop.

```html
<!DOCTYPE html>
<html lang="en">
<head>
<meta charset="utf-8">
<title>K&amp;T Electric Door Hanger</title>
<link href="https://fonts.googleapis.com/css2?family=Inter+Tight:wght@300;400;500;700;800&display=swap" rel="stylesheet">
<style>
  :root {
    --bg: #a3b6d1;
    --panel: #1d1d1f;
    --red: #ee0a0a;
    --white: #ffffff;
    --ink: #111111;
    --copper: #b8643a;
    --bulb: #e0a53a;
  }
  * { margin: 0; padding: 0; box-sizing: border-box; }
  html, body { width: 1122px; height: 1200px; overflow: hidden; }
  body { background: var(--bg); font-family: "Inter Tight", Arial, sans-serif; position: relative; }

  .hanger { position: absolute; top: 94px; width: 434px; height: 1012px; background: var(--panel); overflow: hidden; color: var(--white); }
  .hanger--front { left: 102px; }
  .hanger--back { left: 587px; }

  .abs { position: absolute; }
  .hanger-hole { position: absolute; left: 0; top: 0; }

  .photo-wires { background: radial-gradient(ellipse at 55% 45%, #c9784a 0%, #8a4a2c 45%, #2a2a2c 80%, transparent 100%); }
  .photo-bulb { background: radial-gradient(ellipse at 50% 72%, #f3c35a 0%, #8a6a34 22%, #3b3b40 48%, transparent 72%), linear-gradient(to bottom, #111 0 38%, transparent 38%); border-radius: 0 0 45% 45%; }

  .band-red { position: absolute; left: 0; top: 259px; width: 100%; height: 116px; background: var(--red); }
  .headline { font-weight: 700; letter-spacing: -2px; line-height: 0.98; }
  .front-title { left: 30px; top: 268px; font-size: 46px; color: var(--white); }
  .front-sub { left: 31px; top: 386px; font-size: 25px; font-weight: 400; line-height: 30px; letter-spacing: -0.6px; }

  .grid-line { position: absolute; background: #cfcfcf; }
  .feature-text { font-size: 21px; font-weight: 300; line-height: 23px; letter-spacing: -0.4px; }
  .feature-icon { position: absolute; }

  .offer-box { left: 2px; top: 698px; width: 198px; height: 107px; background: var(--red); }
  .offer-label { left: 30px; top: 712px; font-size: 38px; font-weight: 800; letter-spacing: -1.6px; line-height: 0.92; }
  .offer-value { left: 207px; top: 706px; font-size: 54px; font-weight: 800; letter-spacing: -3px; line-height: 1; }
  .offer-note { left: 212px; top: 765px; font-size: 18px; font-weight: 700; letter-spacing: -0.6px; }

  .contact-strip { position: absolute; left: 0; top: 853px; width: 100%; height: 159px; background: var(--white); color: var(--ink); }
  .contact-row { position: absolute; left: 27px; display: flex; align-items: center; gap: 14px; }
  .contact-phone { top: 34px; font-size: 22px; font-weight: 700; }
  .contact-web { top: 67px; font-size: 17px; font-weight: 400; }
  .contact-mail { top: 95px; font-size: 15.5px; font-weight: 400; }
  .brand-name { position: absolute; left: 270px; top: 40px; width: 140px; font-size: 36px; font-weight: 800; line-height: 0.95; letter-spacing: -1px; color: var(--ink); text-align: center; }

  .band-white { position: absolute; left: 0; top: 259px; width: 100%; height: 125px; background: var(--white); }
  .back-title { left: 28px; top: 287px; font-size: 37px; color: var(--ink); letter-spacing: -2.4px; }
  .back-title .accent { color: var(--red); }
  .back-intro { left: 28px; top: 393px; font-size: 22px; font-weight: 400; line-height: 28px; letter-spacing: -0.6px; }
  .service-list { position: absolute; left: 33px; top: 497px; list-style: none; }
  .service-list li { height: 33.8px; display: flex; align-items: center; font-size: 17.5px; font-weight: 400; letter-spacing: -0.4px; }
  .service-list li::before { content: "›"; color: var(--red); font-size: 20px; width: 22px; font-weight: 500; }
</style>
</head>
<body>

<!-- FRONT -->
<section class="hanger hanger--front">
  <svg class="hanger-hole" width="434" height="259" viewBox="0 0 434 259">
    <g fill="none" stroke="#fff" stroke-width="1.6" stroke-dasharray="14 10">
      <line x1="88" y1="0" x2="184" y2="82"/>
      <circle cx="217" cy="133" r="59"/>
    </g>
  </svg>
  <div class="abs photo-wires" style="left:-40px;top:36px;width:188px;height:223px" role="img" aria-label="Bundle of cut copper electrical cables"></div>

  <div class="band-red"></div>
  <h1 class="abs headline front-title">Need a Reliable<br>Electrician?</h1>
  <div class="abs photo-bulb" style="left:335px;top:259px;width:86px;height:235px" role="img" aria-label="Hanging vintage filament light bulb"></div>

  <p class="abs front-sub">Your Local Electrical<br>Expert is Just Around<br>the Corner!</p>

  <div class="grid-line" style="left:216px;top:505px;width:1px;height:152px"></div>
  <div class="grid-line" style="left:34px;top:588px;width:381px;height:1px"></div>

  <svg class="feature-icon" style="left:30px;top:511px" width="46" height="42" viewBox="0 0 46 42" fill="none" stroke="#ee0a0a" stroke-width="1.8">
    <circle cx="26" cy="24" r="15"/><path d="M26 14v10l6 4"/><path d="M22 7h8M26 7v2"/><path d="M2 20h7M4 25h6M2 30h7"/>
  </svg>
  <p class="abs feature-text" style="left:86px;top:506px">Quick<br>Response<br>Times</p>

  <svg class="feature-icon" style="left:226px;top:508px" width="46" height="46" viewBox="0 0 46 46" fill="none" stroke="#ee0a0a" stroke-width="1.6">
    <path d="M7 3l1.5 3 3 .4-2.2 2 .6 3-2.9-1.5-2.9 1.5.6-3-2.2-2 3-.4z"/>
    <path d="M23 1l1.5 3 3 .4-2.2 2 .6 3-2.9-1.5-2.9 1.5.6-3-2.2-2 3-.4z"/>
    <path d="M39 3l1.5 3 3 .4-2.2 2 .6 3-2.9-1.5-2.9 1.5.6-3-2.2-2 3-.4z"/>
    <circle cx="23" cy="30" r="14"/><circle cx="23" cy="30" r="10"/><path d="M18 28h3v8h-3zM21 29l3-5c1.5 0 2 1 1.5 3h3.5c1 0 1.5 1 1 2l-1.5 5c-.3.7-1 1-1.5 1H21"/>
  </svg>
  <p class="abs feature-text" style="left:282px;top:508px">Quality<br>Workmanship</p>

  <svg class="feature-icon" style="left:28px;top:604px" width="48" height="48" viewBox="0 0 48 48" fill="none" stroke="#ee0a0a" stroke-width="1.8">
    <circle cx="30" cy="13" r="11"/><path d="M32 8h-4a2.5 2.5 0 0 0 0 5h4a2.5 2.5 0 0 1 0 5h-5M30 5v3M30 18v3"/>
    <path d="M2 34l6-3 6 14-6 3z"/><path d="M10 33c4-3 8-3 12-1h8c2 0 2 3 0 3h-8M14 42l6-2c6-1 12-5 16-8 2-1 3 1 2 2l-8 7"/>
  </svg>
  <p class="abs feature-text" style="left:89px;top:608px">Affordable<br>Rates</p>

  <svg class="feature-icon" style="left:233px;top:604px" width="36" height="46" viewBox="0 0 36 46" fill="none" stroke="#ee0a0a" stroke-width="1.8">
    <path d="M22 36H2V2h24v18"/><path d="M7 9h14M7 14h14M7 19h9"/>
    <circle cx="26" cy="28" r="7"/><path d="M23 28l2 2 4-4"/><path d="M22 34v10l4-3 4 3V34"/>
  </svg>
  <p class="abs feature-text" style="left:282px;top:608px">Fully Licensed<br>&amp; Insured</p>

  <div class="abs offer-box"></div>
  <p class="abs offer-label">SPECIAL<br>OFFER</p>
  <p class="abs offer-value">10% OFF</p>
  <p class="abs offer-note">Your First Service Call!</p>

  <footer class="contact-strip">
    <div class="contact-row contact-phone">
      <svg width="20" height="20" viewBox="0 0 24 24" fill="#ee0a0a"><path d="M6.6 10.8a15 15 0 0 0 6.6 6.6l2.2-2.2c.3-.3.7-.4 1-.2 1.1.4 2.3.6 3.6.6.6 0 1 .4 1 1V20c0 .6-.4 1-1 1A17 17 0 0 1 3 4c0-.6.4-1 1-1h3.5c.6 0 1 .4 1 1 0 1.3.2 2.5.6 3.6.1.3 0 .7-.2 1z"/></svg>
      <span>(555) 318-4702</span>
    </div>
    <div class="contact-row contact-web">
      <svg width="14" height="14" viewBox="0 0 24 24"><circle cx="12" cy="12" r="11" fill="#ee0a0a"/><path d="M5 9c3 0 4 2 3 4s1 4 2 6M14 3c0 3 3 3 4 5s-2 4 0 6 3 1 4 0" stroke="#fff" stroke-width="1.6" fill="none"/></svg>
      <span>www.kandtelectric.example</span>
    </div>
    <div class="contact-row contact-mail">
      <svg width="14" height="11" viewBox="0 0 24 18" fill="#ee0a0a"><path d="M0 0h24v18H0z"/><path d="M1 1l11 8 11-8" stroke="#fff" stroke-width="2" fill="none"/></svg>
      <span>info@kandtelectric.example</span>
    </div>
    <p class="brand-name">K&amp;T<br>Electric</p>
  </footer>
</section>

<!-- BACK -->
<section class="hanger hanger--back">
  <svg class="hanger-hole" width="434" height="259" viewBox="0 0 434 259">
    <g fill="none" stroke="#fff" stroke-width="1.6" stroke-dasharray="14 10">
      <line x1="88" y1="0" x2="186" y2="82"/>
      <circle cx="218" cy="133" r="59"/>
    </g>
  </svg>
  <div class="abs photo-bulb" style="left:22px;top:4px;width:95px;height:264px;z-index:2" role="img" aria-label="Hanging vintage filament light bulb"></div>

  <div class="band-white"></div>
  <h2 class="abs headline back-title">Don't Let <span class="accent">Electrical Issues</span><br>Keep You in the Dark!</h2>

  <p class="abs back-intro">From flickering lights to complete<br>system upgrades, we've got all your<br>residential electrical needs covered</p>

  <div class="abs photo-wires" style="left:307px;top:607px;width:160px;height:244px" role="img" aria-label="Bundles of cut copper electrical cables"></div>

  <ul class="service-list">
    <li>Electrical Repairs &amp; Troubleshooting</li>
    <li>Lighting Installation &amp; Upgrades</li>
    <li>Safety Inspections &amp; Code Compliance</li>
    <li>Energy-Efficient Solutions</li>
    <li>24/7 Emergency Services</li>
    <li>Why Choose Us?</li>
    <li>Friendly, Local Service</li>
    <li>Over 30 Years of Experience</li>
    <li>Satisfaction Guaranteed</li>
    <li>Upfront Pricing</li>
  </ul>

  <footer class="contact-strip">
    <div class="contact-row contact-phone">
      <svg width="20" height="20" viewBox="0 0 24 24" fill="#ee0a0a"><path d="M6.6 10.8a15 15 0 0 0 6.6 6.6l2.2-2.2c.3-.3.7-.4 1-.2 1.1.4 2.3.6 3.6.6.6 0 1 .4 1 1V20c0 .6-.4 1-1 1A17 17 0 0 1 3 4c0-.6.4-1 1-1h3.5c.6 0 1 .4 1 1 0 1.3.2 2.5.6 3.6.1.3 0 .7-.2 1z"/></svg>
      <span>(555) 318-4702</span>
    </div>
    <div class="contact-row contact-web">
      <svg width="14" height="14" viewBox="0 0 24 24"><circle cx="12" cy="12" r="11" fill="#ee0a0a"/><path d="M5 9c3 0 4 2 3 4s1 4 2 6M14 3c0 3 3 3 4 5s-2 4 0 6 3 1 4 0" stroke="#fff" stroke-width="1.6" fill="none"/></svg>
      <span>www.kandtelectric.example</span>
    </div>
    <div class="contact-row contact-mail">
      <svg width="14" height="11" viewBox="0 0 24 18" fill="#ee0a0a"><path d="M0 0h24v18H0z"/><path d="M1 1l11 8 11-8" stroke="#fff" stroke-width="2" fill="none"/></svg>
      <span>info@kandtelectric.example</span>
    </div>
    <p class="brand-name">K&amp;T<br>Electric</p>
  </footer>
</section>

</body>
</html>
```